11X17 Poster Drop A Dress Size Challenge

We are having a 21-Day Drop A Dress Size Challenge for our Fitness Studio. We need a poster designed using the template attached as a reference. I have included our Vorenzo Bootcamps logo to put in the poster as well. Please DO NOT use the graphics in the flyer as we are expecting something much better :)
- Size needed 11x17 with bleeding for printing
- We need this made in Photoshop (CS3 friendly) or at least delivered in PS as we might change some text or re-arrange the design later on.

Target Market(s)

Personal Training Studio

Industry/Entity Type

Printing

Colors
0255a3
3377b5
85acd3
f37123
f68e4e
faa54b
f78f20
0692cd
34a7d8

Requirements
Must have
• Must be 11x17 with bleed for printing
• Must be in PS file (CS3 compatible)
• Must include our Vorenzo Bootcamps logo somewhere in the poster
• Must include the information provided in the attached flyer
Nice to have
• Nice to have quality graphics that coincide with the challenge and our logo
Should not have
• Please NO scantily dressed women :)

```html
<!DOCTYPE html>
<html lang="en">
<head>
<meta charset="utf-8">
<title>Drop A Dress Size in 21 Days – Vorenzo Bootcamps</title>
<link rel="stylesheet" href="https://fonts.googleapis.com/css2?family=Alfa+Slab+One&family=Barlow:wght@500;600;700&family=Barlow+Condensed:wght@600;700&display=swap">
<style>
  :root {
    --page-bg: #e9e9e9;
    --poster-dark: #141414;
    --poster-mid: #2a2a2a;
    --band-dark: #0b0b0b;
    --blue: #34a7d8;
    --blue-deep: #0692cd;
    --orange: #f78f20;
    --orange-soft: #faa54b;
    --grey-title: #cfcfcf;
    --text-light: #ffffff;
    --text-dark: #222222;
    --footer-bg: #f4f4f4;
    --rivet: #9a9a9a;
  }
  * { box-sizing: border-box; margin: 0; padding: 0; }
  html, body { width: 861px; height: 1200px; overflow: hidden; background: var(--page-bg); }
  .stage { position: relative; width: 861px; height: 1200px; }
  .poster {
    position: absolute; left: 59px; top: 39px;
    width: 619px; height: 935px;
    transform: scale(1.2); transform-origin: 0 0;
    background: var(--footer-bg);
    font-family: "Barlow", Arial, sans-serif;
    overflow: hidden;
  }
  .hero {
    position: absolute; left: 0; top: 0; width: 619px; height: 745px;
    background: radial-gradient(ellipse at 35% 35%, var(--poster-mid), var(--poster-dark) 70%);
  }
  .hero-photo {
    position: absolute; left: 250px; top: 0; width: 369px; height: 745px;
    background: linear-gradient(180deg, #f2f2f2 0%, #e8e8e8 45%, #d7ad8f 52%, #c99a7a 60%, #6d8fb4 66%, #5b7ea5 100%);
    opacity: .9;
    -webkit-mask-image: linear-gradient(90deg, transparent 0, #000 38%);
            mask-image: linear-gradient(90deg, transparent 0, #000 38%);
  }
  .chevrons { position: absolute; left: 36px; top: 50px; }
  .title-drop {
    position: absolute; left: 83px; top: 40px;
    font-family: "Alfa Slab One", Georgia, serif; font-size: 64px; line-height: 1;
    color: var(--blue); letter-spacing: 1px;
  }
  .title-21 {
    position: absolute; left: 80px; top: 98px;
    font-family: "Alfa Slab One", Georgia, serif; font-size: 100px; line-height: 1;
    color: var(--orange-soft);
  }
  .title-sub {
    position: absolute; left: 210px; top: 110px;
    font-family: "Alfa Slab One", Georgia, serif; font-size: 20px; line-height: 20px;
    color: var(--grey-title); text-transform: uppercase;
  }
  .title-days {
    position: absolute; left: 208px; top: 156px;
    font-family: "Alfa Slab One", Georgia, serif; font-size: 38px; line-height: 1;
    color: var(--orange-soft); letter-spacing: 6px;
  }
  .intro {
    position: absolute; left: 35px; width: 330px;
    color: var(--text-light); font-weight: 600; font-size: 12.6px; line-height: 17.5px;
  }
  .intro-one { top: 222px; }
  .intro-two { top: 305px; width: 300px; }
  .offer-lead {
    position: absolute; left: 30px; top: 405px;
    color: var(--blue); font-weight: 700; font-size: 16.5px; line-height: 20px;
  }
  .benefits {
    position: absolute; left: 0; top: 462px; width: 380px; height: 208px;
    background: linear-gradient(90deg, var(--band-dark) 70%, rgba(11,11,11,0));
    padding: 8px 0 0 30px; color: var(--text-light);
  }
  .benefits-heading { font-weight: 700; font-size: 11.5px; margin-bottom: 6px; }
  .benefit-list { list-style: none; }
  .benefit { display: flex; gap: 5px; font-size: 10.6px; line-height: 12.5px; margin-bottom: 3px; font-weight: 500; }
  .benefit svg { flex: 0 0 20px; margin-top: 1px; }
  .benefit-text { width: 295px; }
  .benefit-text.short { width: 170px; }
  .price-value {
    position: absolute; left: 30px; top: 688px;
    color: var(--blue); font-weight: 700; font-size: 17px;
  }
  .price-now {
    position: absolute; left: 30px; top: 710px;
    color: var(--orange); font-weight: 700; font-size: 19px;
  }
  .rivets { position: absolute; left: 30px; top: 754px; }
  .brand-box {
    position: absolute; left: 368px; top: 702px; width: 222px; height: 70px;
    background: #ffffff; border: 3px solid #111; border-radius: 6px;
    display: flex; align-items: center; justify-content: center;
    font-family: "Barlow Condensed", Arial, sans-serif; font-weight: 700;
    font-size: 26px; color: var(--text-dark); text-transform: uppercase; letter-spacing: 1px;
  }
  .cta {
    position: absolute; left: 30px; top: 778px; width: 210px; text-align: center; color: var(--text-dark);
  }
  .cta-headline { font-weight: 700; font-size: 23px; line-height: 25px; }
  .cta-date { font-size: 14px; font-weight: 500; margin-top: 2px; }
  .cta-claim { font-weight: 700; font-size: 14px; margin-top: 10px; }
  .cta-web, .cta-phone { font-size: 14px; font-weight: 600; line-height: 18px; }
  .cta-phone { font-weight: 500; }
  .prizes {
    position: absolute; right: 40px; top: 813px; text-align: right;
    color: var(--text-dark); font-weight: 700; font-size: 14px; line-height: 21px;
  }
  .prizes .gap { margin-top: 10px; }
</style>
</head>
<body>
<main class="stage">
  <article class="poster">
    <section class="hero">
      <div class="hero-photo" role="img" aria-label="Photo of a woman's slim waist in oversized jeans, pulling the waistband out"></div>

      <svg class="chevrons" width="44" height="132" viewBox="0 0 44 132" aria-hidden="true">
        <g fill="none" stroke="#34a7d8" stroke-width="6" stroke-linejoin="miter">
          <polyline points="4,4 22,20 40,4"/>
          <polyline points="4,30 22,46 40,30"/>
          <polyline points="4,56 22,72 40,56"/>
          <polyline points="4,82 22,98 40,82"/>
          <polyline points="4,108 22,124 40,108"/>
        </g>
      </svg>

      <h1 class="title">
        <span class="title-drop">DROP</span>
        <span class="title-21">21</span>
        <span class="title-sub">A Dress<br>Size In</span>
        <span class="title-days">DAYS</span>
      </h1>

      <p class="intro intro-one">Are you tired of all the health clubs and fitness centers that tell you exactly what you want to hear to get you to join, but once you're a member they forget about you and don't teach you anything about how to get results?</p>
      <p class="intro intro-two">Are you frustrated by all the gimmicks; the pills, powders, shakes and gadgets sold on late night TV that are nothing more than empty promises and slick marketing?</p>

      <p class="offer-lead">If so, then this amazing<br>offer is perfect for you...</p>

      <div class="benefits">
        <p class="benefits-heading">Here's what you get:</p>
        <ul class="benefit-list">
          <li class="benefit">
            <svg width="20" height="20" viewBox="0 0 20 20" aria-hidden="true"><g fill="none" stroke="#fff" stroke-width="1.8" stroke-linecap="round"><circle cx="12" cy="3" r="2" fill="#fff" stroke="none"/><path d="M11 6 8 11l4 2-1 5M8 11l-4 3M10 7l4 3 3-1M2 18h16"/></g></svg>
            <span class="benefit-text">Three weeks worth of Fat Burning Workouts with a Certified Personal Trainer to make sure that you don't spend one minute exercising that doesn't produce results.</span>
          </li>
          <li class="benefit">
            <svg width="20" height="20" viewBox="0 0 20 20" aria-hidden="true"><rect x="2" y="3" width="16" height="15" rx="2" fill="none" stroke="#fff" stroke-width="1.6"/><path d="M2 7h16" stroke="#fff" stroke-width="1.6"/><g fill="#fff"><rect x="5" y="9" width="2" height="2"/><rect x="9" y="9" width="2" height="2"/><rect x="13" y="9" width="2" height="2"/><rect x="5" y="13" width="2" height="2"/><rect x="9" y="13" width="2" height="2"/></g></svg>
            <span class="benefit-text">21 Days of Fat Burning Meal Plans designed by a Registered Dietician to ensure that you reach your goals as quickly as possible.</span>
          </li>
          <li class="benefit">
            <svg width="20" height="20" viewBox="0 0 20 20" aria-hidden="true"><rect x="2" y="3" width="16" height="15" rx="2" fill="none" stroke="#fff" stroke-width="1.6"/><text x="10" y="11" fill="#fff" font-size="6" text-anchor="middle" font-family="Arial, sans-serif">kcal</text></svg>
            <span class="benefit-text">Nutrition Coaching Session to answer all your questions and set you up for success</span>
          </li>
          <li class="benefit">
            <svg width="20" height="20" viewBox="0 0 20 20" aria-hidden="true"><path d="M5 2v16M15 2v16M5 7h10M5 13h10" fill="none" stroke="#fff" stroke-width="1.8"/></svg>
            <span class="benefit-text">21 Days of Lessons to keep you on track to achieving your goal of dropping a dress size</span>
          </li>
        </ul>
      </div>

      <p class="price-value">...You get all this - a $327 Value -</p>
      <p class="price-now">for ONLY $97!</p>
    </section>

    <svg class="rivets" width="330" height="10" viewBox="0 0 330 10" aria-hidden="true">
      <g fill="#9a9a9a">
        <circle cx="5" cy="5" r="3.5"/><circle cx="25" cy="5" r="3.5"/><circle cx="45" cy="5" r="3.5"/><circle cx="65" cy="5" r="3.5"/><circle cx="85" cy="5" r="3.5"/><circle cx="105" cy="5" r="3.5"/><circle cx="125" cy="5" r="3.5"/><circle cx="145" cy="5" r="3.5"/><circle cx="165" cy="5" r="3.5"/><circle cx="185" cy="5" r="3.5"/><circle cx="205" cy="5" r="3.5"/><circle cx="225" cy="5" r="3.5"/><circle cx="245" cy="5" r="3.5"/><circle cx="265" cy="5" r="3.5"/><circle cx="285" cy="5" r="3.5"/><circle cx="305" cy="5" r="3.5"/><circle cx="325" cy="5" r="3.5"/>
      </g>
    </svg>

    <div class="brand-box">Vorenzo Bootcamps</div>

    <section class="cta">
      <p class="cta-headline">HURRY! SPACE IS LIMITED LADIES!!</p>
      <p class="cta-date">Starts April 6th 2015</p>
      <p class="cta-claim">CLAIM YOUR SPOT NOW</p>
      <p class="cta-web">www.vorenzobootcamps.com</p>
      <p class="cta-phone">Call 303-555-0172</p>
    </section>

    <section class="prizes">
      <p>WINNER GETS $100 Cash,</p>
      <p>A NEW DRESS (Up to $100 Value)</p>
      <p class="gap">AND A FREE PHOTO SHOOT!</p>
      <p>($150 Value)</p>
    </section>
  </article>
</main>
</body>
</html>
```